Business Card Design - Carrington Hill Lodge

We are looking at a new design for our business cards that has a modern and professional look. We run a residential aged care facility focussing on the care of residents. The cards will be used for potential clients, consultants and business opportunities in this sector. Blue and white is our main colours and would to see these colours incorporated in the design.
Industry/Entity Type
Business
Contact Information for Business Card
Carrington Hill Lodge, Darren Pelham, dpelham@carringtonhilllodge.com.au, Finance Manager, 0491 736 208, BCom, 48 Yarrabee Way, Yarrabee Park, Qld 4182.

```html
<!DOCTYPE html>
<html lang="en">
<head>
<meta charset="utf-8">
<title>Darren Pelham – Carrington Hill Lodge</title>
<link rel="stylesheet" href="https://fonts.googleapis.com/css2?family=Gentium+Book+Plus:wght@400&display=swap">
<style>
  :root {
    --page: #ffffff;
    --card: #dff0f2;
    --card-light: #eef8f9;
    --ink-blue: #3b86a6;
    --band-blue: #4188a8;
    --icon-grey: #a8a39c;
    --tag-grey: #8f8a84;
    --white: #ffffff;
  }
  html, body {
    margin: 0;
    width: 1200px;
    height: 741px;
    overflow: hidden;
    background: var(--page);
  }
  .canvas {
    position: relative;
    width: 1200px;
    height: 741px;
    font-family: "Gentium Book Plus", "Palatino Linotype", serif;
  }
  .card {
    position: absolute;
    left: 15px;
    top: 19px;
    width: 1170px;
    height: 705px;
    background:
      radial-gradient(ellipse 260px 140px at 300px 120px, var(--card-light), transparent),
      radial-gradient(ellipse 220px 180px at 560px 560px, var(--card-light), transparent),
      radial-gradient(ellipse 300px 120px at 900px 80px, var(--card-light), transparent),
      var(--card);
    overflow: hidden;
  }
  .band {
    position: absolute;
    left: 0;
    bottom: 0;
    width: 100%;
    height: 52px;
    background: var(--band-blue);
  }
  .person-name {
    position: absolute;
    left: 80px;
    top: 142px;
    margin: 0;
    font-size: 92px;
    font-weight: 400;
    line-height: 1;
    color: var(--ink-blue);
    white-space: nowrap;
  }
  .job-title {
    position: absolute;
    left: 83px;
    top: 264px;
    margin: 0;
    font-size: 58px;
    font-weight: 400;
    line-height: 1;
    color: var(--ink-blue);
  }
  .contact-list {
    position: absolute;
    left: 131px;
    top: 348px;
    margin: 0;
    padding: 0;
    list-style: none;
    color: var(--ink-blue);
    font-size: 29px;
    line-height: 35px;
  }
  .contact-item {
    position: relative;
    padding-left: 63px;
    margin-bottom: 30px;
    white-space: nowrap;
  }
  .contact-item.address { padding-left: 57px; }
  .contact-icon {
    position: absolute;
    left: 0;
    top: -3px;
    width: 44px;
    height: 44px;
  }
  .brand {
    position: absolute;
    left: 697px;
    top: 300px;
    width: 400px;
    text-align: center;
  }
  .brand-name {
    margin: 0;
    font-size: 38px;
    font-weight: 400;
    line-height: 1.1;
    color: var(--ink-blue);
    white-space: nowrap;
  }
  .brand-tagline {
    margin: 12px 0 0;
    font-size: 22px;
    color: var(--tag-grey);
  }
</style>
</head>
<body>
<main class="canvas">
  <section class="card">
    <h1 class="person-name">Darren Pelham</h1>
    <p class="job-title">Finance Manager</p>

    <ul class="contact-list">
      <li class="contact-item phone">
        <svg class="contact-icon" viewBox="0 0 44 44" aria-hidden="true">
          <circle cx="22" cy="22" r="22" fill="var(--icon-grey)"/>
          <path d="M15 12c1-1 2.5-1 3.3.2l2.2 3.3c.6 1 .4 2.1-.4 2.8l-1.5 1.2c1 2.4 2.9 4.4 5.3 5.5l1.3-1.5c.7-.8 1.9-1 2.8-.3l3.3 2.3c1.1.8 1.2 2.4.2 3.3l-1.6 1.5c-1.4 1.3-3.5 1.6-5.2.8-5.2-2.5-9.3-6.7-11.6-12-.7-1.7-.3-3.6 1-4.9z" fill="var(--white)"/>
        </svg>
        0491 736 208
      </li>
      <li class="contact-item email">
        <svg class="contact-icon" viewBox="0 0 44 44" aria-hidden="true">
          <circle cx="22" cy="22" r="22" fill="var(--icon-grey)"/>
          <rect x="11" y="14" width="22" height="16" fill="none" stroke="var(--white)" stroke-width="2"/>
          <path d="M11 14l11 9 11-9M11 30l8-8M33 30l-8-8" fill="none" stroke="var(--white)" stroke-width="2"/>
        </svg>
        dpelham@carringtonhilllodge.com.au
      </li>
      <li class="contact-item address">
        <svg class="contact-icon" viewBox="0 0 44 44" aria-hidden="true">
          <circle cx="22" cy="22" r="22" fill="var(--icon-grey)"/>
          <path d="M22 11l-12 11h3.5v11h6.5v-7h4v7h6.5V22H34z" fill="var(--white)"/>
        </svg>
        BCom, 48 Yarrabee Way,<br>Yarrabee Park, Qld 4182
      </li>
    </ul>

    <div class="brand">
      <p class="brand-name">Carrington Hill Lodge</p>
      <p class="brand-tagline">Caring, Respectful, Personal</p>
    </div>

    <div class="band"></div>
  </section>
</main>
</body>
</html>
```